Bref créative
BRN Tek
B-cards, letter head and envelopes
I need single sided standard sized Business Card [3.5" x 2"]
use same font or others...other fonts are welcome
Simple
Gareth Pembly
CEO
482 Harlowe Street, Suite 1730
San Francisco, California 94111
gpembly@brnqel.com
brnqel.com
-use this logo in the business cards, letterhead and envelopes.
-we are looking for designs with and with out a water mark using parts or the entire logo.

```html
<!DOCTYPE html>
<html lang="en">
<head>
<meta charset="utf-8">
<title>BRN Tek – Stationery Set</title>
<link rel="stylesheet" href="https://fonts.googleapis.com/css2?family=Open+Sans:wght@400;600;700;800&display=swap">
<style>
  :root {
    --green: #8cc63f;
    --green-dark: #76ad2c;
    --blue: #1f4e9c;
    --ink: #3a3a3a;
    --paper: #ffffff;
    --edge: #d4d4d4;
    --faint: #f1f7e8;
    --bg: #ffffff;
  }
  * { box-sizing: border-box; margin: 0; padding: 0; }
  html, body { width: 1200px; height: 737px; overflow: hidden; background: var(--bg); }
  body { position: relative; font-family: "Open Sans", Arial, sans-serif; color: var(--ink); }

  .sheet { position: absolute; background: var(--paper); border: 1px solid var(--edge); box-shadow: 0 1px 3px rgba(0,0,0,.12); overflow: hidden; }
  .swoosh { position: absolute; top: 0; right: 0; }

  .wordmark { position: absolute; font-weight: 800; color: var(--green); letter-spacing: 1px; line-height: 1; }
  .wordmark.on-green { color: var(--paper); }

  /* Letterhead */
  .letterhead { left: 19px; top: 19px; width: 528px; height: 682px; }
  .letterhead .wordmark { left: 18px; top: 24px; font-size: 30px; }
  .letterhead .watermark { position: absolute; left: 0; right: 0; top: 300px; text-align: center; font-size: 150px; font-weight: 800; color: var(--faint); letter-spacing: 6px; line-height: 1; }
  .letterhead .footer { position: absolute; left: 0; right: 0; bottom: 18px; text-align: center; color: var(--blue); font-size: 8.5px; line-height: 1.5; }

  /* Envelope front */
  .envelope-front { left: 576px; top: 19px; width: 612px; height: 288px; }
  .envelope-front .wordmark { left: 18px; top: 22px; font-size: 26px; }
  .envelope-front .return-address { position: absolute; left: 18px; top: 232px; color: var(--blue); font-size: 9px; }

  /* Envelope back */
  .envelope-back { left: 576px; top: 336px; width: 612px; height: 216px; background: var(--green); border-color: var(--green-dark); }
  .envelope-back svg { position: absolute; left: 0; top: 0; }
  .envelope-back .caption { position: absolute; left: 0; right: 0; top: 62px; text-align: center; color: var(--paper); font-size: 6.5px; }
  .envelope-back .wordmark { left: 0; right: 0; top: 74px; text-align: center; font-size: 38px; }

  /* Business card front */
  .card-front { left: 576px; top: 576px; width: 252px; height: 139px; }
  .card-front .wordmark { left: 10px; top: 16px; font-size: 18px; }
  .card-front .person { position: absolute; left: 10px; top: 62px; }
  .card-front .name { color: var(--green); font-weight: 700; font-size: 10px; }
  .card-front .role { font-size: 7px; color: var(--ink); }
  .card-front .contact { position: absolute; left: 130px; top: 58px; font-size: 6px; line-height: 1.5; color: var(--ink); }

  /* Business card back */
  .card-back { left: 845px; top: 576px; width: 254px; height: 139px; background: var(--green); border-color: var(--green-dark); }
  .card-back .wordmark { left: 0; right: 0; top: 48px; text-align: center; font-size: 34px; }
  .card-back .tagline { position: absolute; left: 0; right: 0; top: 88px; text-align: center; color: var(--paper); font-size: 6px; }
</style>
</head>
<body>

<section class="sheet letterhead">
  <svg class="swoosh" width="528" height="70" viewBox="0 0 528 70" aria-hidden="true">
    <path d="M150 0 H528 V52 C440 20 300 8 150 0 Z" fill="var(--green)"/>
    <path d="M120 2 C300 12 440 30 528 64" fill="none" stroke="var(--blue)" stroke-width="3"/>
  </svg>
  <div class="wordmark">BRN</div>
  <div class="watermark" aria-hidden="true">BRN</div>
  <div class="footer">
    <p>482 Harlowe Street, Suite 1730, San Francisco, California 94111</p>
    <p>Toll free: 800.413.7720 | Phone: 415.286.0193 | Fax: 415.286.0194 | www.brnqel.com</p>
  </div>
</section>

<section class="sheet envelope-front">
  <svg class="swoosh" width="612" height="60" viewBox="0 0 612 60" aria-hidden="true">
    <path d="M220 0 H612 V44 C520 16 380 6 220 0 Z" fill="var(--green)"/>
    <path d="M190 2 C380 10 520 26 612 56" fill="none" stroke="var(--blue)" stroke-width="3"/>
  </svg>
  <div class="wordmark">BRN</div>
  <p class="return-address">482 Harlowe Street, Suite 1730, San Francisco, California 94111</p>
</section>

<section class="sheet envelope-back">
  <svg width="612" height="216" viewBox="0 0 612 216" aria-hidden="true">
    <path d="M0 140 L40 216 H0 Z M612 140 L572 216 H612 Z" fill="var(--paper)"/>
    <path d="M0 0 L306 170 L612 0" fill="none" stroke="var(--green-dark)" stroke-width="1"/>
  </svg>
  <p class="caption">visit brnqel.com</p>
  <div class="wordmark on-green">BRN</div>
</section>

<section class="sheet card-front">
  <svg class="swoosh" width="252" height="30" viewBox="0 0 252 30" aria-hidden="true">
    <path d="M60 0 H252 V22 C200 8 130 3 60 0 Z" fill="var(--green)"/>
    <path d="M50 1 C130 5 200 12 252 28" fill="none" stroke="var(--blue)" stroke-width="1.5"/>
  </svg>
  <div class="wordmark">BRN</div>
  <div class="person">
    <p class="name">Gareth Pembly</p>
    <p class="role">CEO</p>
  </div>
  <div class="contact">
    <p>482 Harlowe Street, Suite 1730</p>
    <p>San Francisco, California 94111</p>
    <p>Phone: 415.286.0193</p>
    <p>Fax: 415.286.0194</p>
    <p>gpembly@brnqel.com</p>
    <p>brnqel.com</p>
  </div>
</section>

<section class="sheet card-back">
  <div class="wordmark on-green">BRN</div>
  <p class="tagline">brnqel.com</p>
</section>

</body>
</html>
```